Happy Birthday Postcard for law firm for existing clients

Need a postcard that will go out to our current clients on their birthdays. Prefer to have our logo incorporated as part of the design so it reminds them about our business. The back needs to say "Happy Birthday from the team at Brantley Law Firm."

We are a law firm that services local clients. Needs to be mailed so the backside right half needs to be left blank except the return address (in NEEDS below) so it can be mailed with a mailing label.

Target Market(s)

existing customers, varying age range and demographic profile

Industry/Entity Type

Legal

Font styles to use
Sans Serif
Script

Colors

Designer to choose colors to be used in the design.

Requirements
Must have
• Our logo preferrably on the front (can be modified or added to so it fits a birthday message. And needs to be mailed so the back right side needs to be left open for address labels. The firms return address is
• Brantley Law Firm
• 7150 W Copperfield Ave
• Springfield, MO 65817
• Needs to have the text included in the project description on the back, or some close iteration of it if space is limited.
Nice to have
• Some illustration or graphic on the front with the logo that shows it is a birthday postcard

```html
<!DOCTYPE html>
<html lang="en">
<head>
<meta charset="utf-8">
<title>Birthday Postcard – Brantley Law Firm</title>
<link rel="stylesheet" href="https://fonts.googleapis.com/css2?family=Great+Vibes&family=Poiret+One&family=Marcellus&family=Montserrat:wght@400&family=PT+Sans:ital,wght@0,400;1,700&family=Arimo&display=swap">
<style>
  :root {
    --backdrop: #8a5e3c;
    --card: #ffffff;
    --panel-grey: #e6e7e8;
    --ink: #111111;
    --slate: #595a5f;
    --lavender: #8e92b5;
    --muted: #6d6e71;
    --gold: #e39a1d;
    --gold-light: #f2c418;
    --petal-pink: #ee8fbf;
    --petal-white: #f7f2ea;
    --leaf-green: #8fae6a;
  }
  * { box-sizing: border-box; margin: 0; padding: 0; }
  html, body { width: 810px; height: 1200px; overflow: hidden; }
  body { background: var(--backdrop); position: relative; }

  .postcard {
    position: absolute;
    left: 52px;
    width: 696px;
    height: 540px;
    background: var(--card);
    overflow: hidden;
  }
  .postcard--front { top: 46px; }
  .postcard--back { top: 614px; }

  /* Front */
  .front-photo {
    position: absolute; inset: 0;
    background:
      radial-gradient(ellipse 30% 35% at 68% 25%, var(--petal-pink) 0%, rgba(238,143,191,0.6) 60%, transparent 100%),
      radial-gradient(ellipse 30% 35% at 30% 55%, var(--petal-white) 0%, rgba(247,242,234,0.7) 60%, transparent 100%),
      radial-gradient(circle at 58% 68%, #ffffff 0%, rgba(255,255,255,0.6) 18%, transparent 40%),
      linear-gradient(120deg, #e8efe0 0%, #f4f4ee 40%, var(--leaf-green) 100%);
  }
  .front-greeting {
    position: absolute; left: 30px; top: 448px;
    font-family: "Great Vibes", cursive;
    font-size: 40px; color: #ffffff; line-height: 1;
  }
  .front-signoff {
    position: absolute; left: 27px; top: 500px;
    font-family: "Poiret One", sans-serif;
    font-size: 17px; color: #ffffff;
  }
  .front-brand {
    position: absolute; right: 40px; top: 476px;
    font-family: "Montserrat", sans-serif;
    font-weight: 400; font-size: 38px; letter-spacing: 1px;
    color: #ffffff; line-height: 1;
  }

  /* Back */
  .back-greeting {
    position: absolute; left: 26px; top: 22px;
    font-family: "Great Vibes", cursive;
    font-size: 56px; color: var(--gold); line-height: 1.1;
  }
  .back-from {
    position: absolute; left: 0; width: 376px; top: 94px;
    text-align: center;
    font-family: "Marcellus", serif;
    color: var(--lavender);
  }
  .back-from__lead { font-size: 23px; display: block; line-height: 1.35; }
  .back-from__firm { font-size: 24px; display: block; line-height: 1.35; }

  .back-brand {
    position: absolute; left: 38px; width: 274px; top: 262px;
    text-align: center;
    font-family: "Montserrat", sans-serif;
    font-weight: 400; font-size: 32px; color: var(--slate); line-height: 1;
    white-space: nowrap;
  }
  .brand-rule {
    position: absolute; left: 38px; top: 316px; width: 274px; height: 4px;
    border-radius: 2px;
    background: linear-gradient(90deg, var(--gold), var(--gold-light), var(--gold));
  }
  .return-address {
    position: absolute; left: 38px; width: 274px; top: 338px;
    text-align: center; font-family: "PT Sans", sans-serif; font-style: normal;
  }
  .return-address__label {
    font-style: italic; font-weight: 700; font-size: 16px; color: var(--muted);
    margin-bottom: 6px;
  }
  .return-address__line { font-size: 16px; color: var(--ink); line-height: 1.3; }

  .mail-zone {
    position: absolute; background: var(--panel-grey);
    font-family: "Arimo", sans-serif; font-size: 19px; color: var(--ink);
    text-align: center; line-height: 1.3;
  }
  .mail-zone--postage { left: 523px; top: 18px; width: 155px; height: 155px; padding-top: 68px; }
  .mail-zone--address { left: 337px; top: 173px; width: 341px; height: 271px; padding-top: 36px; }
  .mail-zone--barcode { left: 87px; top: 443px; width: 591px; height: 78px; padding-top: 28px; }
</style>
</head>
<body>
  <section class="postcard postcard--front">
    <div class="front-photo" role="img" aria-label="Photograph of a pink and a white lotus blossom in soft sunlight against blurred green foliage"></div>
    <p class="front-greeting">Happy Birthday</p>
    <p class="front-signoff">from the team at Brantley Law Firm</p>
    <p class="front-brand">BRANTLEY LAW</p>
  </section>

  <section class="postcard postcard--back">
    <h1 class="back-greeting">Happy Birthday</h1>
    <p class="back-from">
      <span class="back-from__lead">from the team at</span>
      <span class="back-from__firm">BRANTLEY LAW FIRM</span>
    </p>
    <p class="back-brand">BRANTLEY LAW</p>
    <div class="brand-rule"></div>
    <address class="return-address">
      <p class="return-address__label">Return address</p>
      <p class="return-address__line">Brantley Law Firm</p>
      <p class="return-address__line">7150 W Copperfield Ave</p>
      <p class="return-address__line">Springfield, MO 65817</p>
    </address>

    <div class="mail-zone mail-zone--postage">Postage<br>Area</div>
    <div class="mail-zone mail-zone--address">Address Area</div>
    <div class="mail-zone mail-zone--barcode">Barcode Area</div>
  </section>
</body>
</html>
```